[Design ONLY] Design for our Ecommerce business website

We require a web design for our ecommerce business website. We sell textbooks, Computer & Accessories, Gifts and stationery and Laptop/IT support service etc
Requirement:
We Require 3 pages for each design: Homepage, Product page and Payment page
Design Approach:
Design UI to be have a modern and professional feel and user experience must be good.
Responsive web design approach.
1. Home page
- Logo/Heading
- Navigation links to other pages eg. About us
- Appropriate images/banners
- A special offer
- Recent News
Include an overview of the business:
- provide general information
- contact information
- links to social media
- Frequently Asked Questions (FAQ) page
Publish store policies and make sure they are not too difficult to find:
- shipping and return policies
- outline the return process and what products can be returned
- provide easy access to a privacy policy that covers shoppers’ personal and financial information (this is crucial)
2. Product
Product Pages should include:
- Pictures, descriptions, order and price information for your products and/or services.
- Navigation links to other pages, especially home, about us, order and other product pages.
- Links to a shopping cart
- Add to wishlist
- Related or recommend products
3. Payment
- Standard payment form with payment integration with Quillo and Vendora.
- Shipping or Self Collection fee
User Experience Aspect:
Well-Defined Product Categories
a. The top level of navigation should show the set of categories that the site offers. Group products into categories and subcategories. Category labels work best as single words that describe the range of products, so shoppers can scan through them and instantly understand what they represent.
Product Search
a. Build a search function that helps them easily find what they are looking for.
Make search omnipresent: Put the search box on every page and in familiar locations. The box should be visible, quickly recognizable, and easy to use.
b. Allow sorting and filtering of results: Let shoppers sort search results based on various criteria (best sellers, highest or lowest price, product rating, newest item, etc.) as well as eliminate items that do not fit within a certain category.
Product Quick view
a. A “quick view” reduces the time it takes for shoppers to find the right product by eliminating unnecessary page loads. Also, be sure to include a prominently positioned “Add to Cart” button as well as a “Save to Wishlist” functionality.
b. Show Related and Recommended Products. This can be displayed on a product detail page.
Target Market(s)
university students
Number of Pages Required
3 page
Font styles to use
Requirements
Must have
- Note * its a university store. not a normal ecommerce shop*
Do include design for the 3 pages specified. Homepage, product page and payment page.

```html
<!DOCTYPE html>
<html lang="en">
<head>
<meta charset="utf-8">
<title>Unicampus Store — Home</title>
<link href="https://fonts.googleapis.com/css2?family=Montserrat:wght@400;500;600;700;800&display=swap" rel="stylesheet">
<style>
:root{
  --navy:#1f2a63;
  --gold:#f0b90b;
  --ink:#1d1d1d;
  --muted:#6b6b6b;
  --line:#d9d9d9;
  --white:#ffffff;
  --soft:#f4f4f4;
  --footer-line:#5a6394;
}
*{box-sizing:border-box;margin:0;padding:0}
html,body{width:1200px;height:2953px;overflow:hidden}
body{font-family:'Montserrat',sans-serif;color:var(--ink);background:var(--white);position:relative}
.wrap{width:900px;margin:0 auto;position:relative}
a{color:inherit;text-decoration:none}

/* top strip */
.promise-bar{height:34px;border-bottom:1px solid var(--line)}
.promise-bar .wrap{display:flex;height:34px;width:910px;border-left:1px solid var(--line);border-right:1px solid var(--line)}
.promise{flex:1;display:flex;align-items:center;justify-content:center;gap:10px;font-size:10.5px;letter-spacing:.3px;color:#444;border-right:1px solid var(--line)}
.promise:last-child{border-right:none}
.promise svg{width:14px;height:14px}

/* header */
.site-header{height:101px}
.site-header .wrap{display:flex;align-items:center;height:101px}
.brand{width:256px;font-weight:700;font-size:22px;color:var(--navy);line-height:1.05}
.brand small{display:block;font-size:10px;font-weight:700;letter-spacing:1px;margin-top:3px}
.search{display:flex;width:454px;height:42px;border:1px solid #bbb}
.search .field{flex:1;font-size:12px;color:#777;display:flex;align-items:center;padding-left:10px}
.search .cat{width:170px;font-size:12px;color:#777;display:flex;align-items:center;justify-content:space-between;padding:0 18px;border-left:1px solid #bbb;margin:12px 0;line-height:16px}
.search .go{width:53px;background:var(--gold);margin:-1px -1px -1px 0;display:flex;align-items:center;justify-content:center}
.socials{display:flex;gap:10px;margin-left:auto}
.dot{width:31px;height:31px;border:1.5px solid #444;border-radius:50%}

/* nav */
.main-nav{height:55px;background:var(--navy)}
.main-nav .wrap{display:flex;height:55px;align-items:center}
.main-nav a{color:var(--white);font-size:13px;font-weight:600;letter-spacing:.6px;margin-right:43px;height:55px;display:flex;align-items:center;position:relative}
.main-nav a.active::after{content:"";position:absolute;left:0;bottom:0;width:68px;height:4px;background:var(--gold)}
.cart{margin-left:auto;background:var(--gold);color:var(--white);font-size:13px;font-weight:700;height:55px;width:132px;display:flex;align-items:center;justify-content:center;gap:8px;letter-spacing:.5px}

/* hero */
.hero{height:455px;position:relative;background:linear-gradient(100deg,#6b5a45 0%,#7a6a52 30%,#8a7a63 50%,#a79680 100%)}
.hero-photo{position:absolute;right:0;top:0;width:620px;height:455px;background:radial-gradient(ellipse at 60% 40%,#eeeeee 0 16%,#3b6bb8 34%,#24488f 58%,rgba(122,106,82,0) 82%)}
.hero-copy{position:absolute;left:150px;top:98px;color:var(--white)}
.hero-copy .kicker{font-size:18px;font-weight:700;letter-spacing:1px}
.hero-copy h1{font-size:48px;font-weight:800;line-height:58px;margin-top:20px}
.hero-copy .cta{display:inline-block;margin-top:24px;color:var(--gold);font-size:31px;font-weight:800;border-bottom:2px solid var(--gold);line-height:36px}
.arrow{position:absolute;top:180px;width:49px;height:49px;border:2px solid var(--white);border-radius:50%;display:flex;align-items:center;justify-content:center}
.arrow.left{left:23px}.arrow.right{right:24px}

/* category tiles */
.tiles{display:flex;gap:23px;margin-top:53px;width:908px;margin-left:149px}
.tile{width:285px;height:217px;position:relative;padding:56px 0 0 21px}
.tile.gifts{background:linear-gradient(135deg,#3a2b2b,#b0403f 35%,#e4c04b 55%,#3b6fb3 80%,#2b2b2b)}
.tile.laptop{background:linear-gradient(135deg,#1d8fd9,#4fb4ee 60%,#9fd4f4)}
.tile.books{background:linear-gradient(90deg,#f3f3f3 0 35%,#7d4fa8 45%,#4a9de0 60%,#e04b7a 80%,#f07b3a)}
.tile h3{font-size:22px;font-weight:400;letter-spacing:1px;line-height:31px;color:var(--white)}
.tile h3 b{font-weight:700}
.tile.books h3{color:var(--ink)}
.tile .btn{display:inline-block;margin-top:14px;background:var(--navy);color:var(--white);font-size:12px;font-weight:700;padding:7px 17px;letter-spacing:.4px}

/* section heads */
.section-head{position:absolute;left:151px}
.section-head h2{font-size:25px;font-weight:700;letter-spacing:.8px}
.section-head .rule{height:3px;background:var(--gold);margin-top:14px}
.pager{position:absolute;right:155px;display:flex;gap:10px}
.pager span{width:30px;height:30px;border:1.5px solid #333;border-radius:50%;display:flex;align-items:center;justify-content:center}

/* product cards */
.card{position:absolute;width:204px}
.card .img{height:239px}
.card h4{font-size:15px;font-weight:700;padding:0 0 10px 0;border-bottom:1.5px solid #e2e2e2;margin:22px 0 0}
.card .price{font-size:20px;color:#444;margin-top:14px}
.card.rated .price{margin-top:20px}
.stars{color:var(--gold);font-size:12px;letter-spacing:4px;margin-top:6px}
.add{display:inline-block;background:var(--navy);color:var(--white);font-size:11px;font-weight:700;padding:7px 10px;margin-top:14px}
.card.rated .add{margin-top:20px}

.promo{position:absolute;left:610px;top:1083px;width:428px;height:365px;background:linear-gradient(160deg,#5b6a7a,#39475a 60%,#2c3644);text-align:center;color:var(--white)}
.promo h3{font-size:25px;font-weight:700;line-height:32px;margin-top:25px;letter-spacing:.6px}
.promo .device{width:250px;height:170px;margin:22px auto 0;background:linear-gradient(135deg,#1e2a3a,#3a7ac9 50%,#cfd7df)}
.promo .shop{display:inline-block;background:var(--gold);padding:14px 34px;font-size:15px;font-weight:700;margin-top:6px}

.divider{position:absolute;left:0;top:2091px;width:1200px;height:1px;background:var(--line)}

/* news */
.news{position:absolute;top:2216px;width:279px}
.news .img{height:169px;position:relative}
.news .date{position:absolute;left:0;bottom:0;background:var(--navy);color:var(--white);width:50px;height:50px;text-align:center;font-size:22px;font-weight:600;line-height:24px;padding-top:6px}
.news .date small{display:block;font-size:9px;line-height:10px;font-weight:500}
.news h5{font-size:13px;font-weight:700;margin:20px 0 0 6px;letter-spacing:.3px}
.news p{font-size:12.5px;color:#555;line-height:21px;margin:10px 0 0 6px}

/* footer */
.site-footer{position:absolute;left:0;top:2549px;width:1200px;height:404px;background:var(--navy);color:var(--white)}
.foot-brand{position:absolute;left:159px;top:47px;font-size:22px;font-weight:700;line-height:1.05}
.foot-brand small{display:block;font-size:10px;font-weight:700;letter-spacing:1px;margin-top:3px}
.foot-about{position:absolute;left:158px;top:130px;width:222px;font-size:12px;line-height:18px}
.newsletter{position:absolute;left:404px;top:58px;display:flex;align-items:center}
.newsletter h6{font-size:16px;font-weight:700;letter-spacing:.5px;width:311px}
.newsletter .email{width:252px;height:43px;background:#f1f1f1;color:#777;font-size:14px;display:flex;align-items:center;padding-left:20px}
.newsletter .submit{width:83px;height:43px;background:var(--gold);font-size:13px;font-weight:700;display:flex;align-items:center;justify-content:center}
.foot-rule{position:absolute;left:412px;top:133px;width:638px;height:1px;background:var(--footer-line)}
.foot-col{position:absolute;top:178px;font-size:11.5px}
.foot-col h6{color:var(--gold);font-size:11.5px;font-weight:700;margin-bottom:13px}
.foot-col li{list-style:none;font-weight:600;margin-bottom:13px;padding-left:13px;position:relative}
.foot-col li::before{content:"";position:absolute;left:0;top:3px;border-left:5px solid var(--gold);border-top:4px solid transparent;border-bottom:4px solid transparent}
.contact-row{display:flex;gap:15px;margin-bottom:13px;font-weight:600;line-height:14px}
.contact-row svg{width:12px;height:14px;flex:none}
.foot-bottom{position:absolute;left:152px;top:338px;width:896px;height:1px;background:var(--footer-line)}
.copyright{position:absolute;left:152px;top:364px;font-size:13px}
.foot-social{position:absolute;right:153px;top:356px;display:flex;gap:13px}
.foot-social span{width:29px;height:29px;border:1.5px solid var(--gold);border-radius:50%}
</style>
</head>
<body>

<div class="promise-bar"><div class="wrap">
  <div class="promise"><svg viewBox="0 0 16 16"><path d="M1 3h9v8H1zM10 6h3l2 3v2h-5z" fill="#f0b90b"/></svg>FREE SHIPPING ON ALL ORDER</div>
  <div class="promise"><svg viewBox="0 0 16 16"><rect x="1" y="4" width="14" height="8" fill="none" stroke="#f0b90b" stroke-width="1.6"/><circle cx="8" cy="8" r="2" fill="#f0b90b"/></svg>100% MONEY BACK GUARANTEE</div>
  <div class="promise"><svg viewBox="0 0 16 16"><circle cx="8" cy="8" r="6" fill="none" stroke="#f0b90b" stroke-width="1.6"/><path d="M8 5v3h2" stroke="#f0b90b" stroke-width="1.6" fill="none"/></svg>ONLINE SUPPORT 24/7</div>
</div></div>

<header class="site-header"><div class="wrap">
  <div class="brand">Unicampus<br>Store<small>EST. 1968</small></div>
  <div class="search">
    <div class="field">Search</div>
    <div class="cat">All Categories <svg width="8" height="5" viewBox="0 0 8 5"><path d="M0 0h8L4 5z" fill="#333"/></svg></div>
    <div class="go"><svg width="14" height="14" viewBox="0 0 14 14"><circle cx="6" cy="6" r="4.3" fill="none" stroke="#fff" stroke-width="2"/><path d="M9 9l4 4" stroke="#fff" stroke-width="2"/></svg></div>
  </div>
  <div class="socials" aria-label="Social media links"><span class="dot"></span><span class="dot"></span><span class="dot"></span><span class="dot"></span></div>
</div></header>

<nav class="main-nav"><div class="wrap">
  <a class="active">TEXTBOOKS</a><a>COMPUTER &amp; ACCESSORIES</a><a>GIFTS &amp; STATIONERY</a><a>LAPTOP/IT SUPPORT</a>
  <div class="cart"><svg width="14" height="12" viewBox="0 0 14 12"><path d="M0 1h3l2 7h7l2-5H4" fill="none" stroke="#fff" stroke-width="1.6"/><circle cx="6" cy="10.5" r="1.2" fill="#fff"/><circle cx="11" cy="10.5" r="1.2" fill="#fff"/></svg>CART (0)</div>
</div></nav>

<section class="hero">
  <div class="hero-photo" role="img" aria-label="Gift box wrapped in blue paper with a ribbon, beside flowers on burlap"></div>
  <div class="hero-copy">
    <div class="kicker">NEW OFFERS !</div>
    <h1>30% offer<br>for new customers</h1>
    <a class="cta">SHOP NOW</a>
  </div>
  <span class="arrow left"><svg width="14" height="22" viewBox="0 0 14 22"><path d="M12 1L2 11l10 10" fill="none" stroke="#fff" stroke-width="2"/></svg></span>
  <span class="arrow right"><svg width="14" height="22" viewBox="0 0 14 22"><path d="M2 1l10 10L2 21" fill="none" stroke="#fff" stroke-width="2"/></svg></span>
</section>

<div class="tiles">
  <div class="tile gifts" role="img" aria-label="Coloured pencils arranged in a circle"><h3>GIFTS &amp;<br><b>STATIONARY</b></h3><span class="btn">SHOP NOW</span></div>
  <div class="tile laptop" role="img" aria-label="Laptops and tablets on a blue background"><h3>LAPTOP<br><b>SUPPORT</b></h3><span class="btn">SHOP NOW</span></div>
  <div class="tile books" role="img" aria-label="Stack of subject textbooks"><h3>TEXT<br><b>BOOKS</b></h3><span class="btn">SHOP NOW</span></div>
</div>

<div class="section-head" style="top:998px"><h2>SPECIAL OFFERS</h2><div class="rule" style="width:278px"></div></div>
<div class="pager" style="top:1009px"><span><svg width="8" height="12"><path d="M7 1L2 6l5 5" fill="none" stroke="#333" stroke-width="1.5"/></svg></span><span><svg width="8" height="12"><path d="M1 1l5 5-5 5" fill="none" stroke="#333" stroke-width="1.5"/></svg></span></div>

<div class="card" style="left:159px;top:1083px"><div class="img" role="img" aria-label="Laptop product photo" style="background:linear-gradient(180deg,#f1f1f1,#e6e6e6)"></div><h4>Product Name 1</h4><div class="price">$ 61.19</div><a class="add">Add to Cart</a></div>
<div class="card" style="left:386px;top:1083px"><div class="img" role="img" aria-label="Leather travel bag product photo" style="background:linear-gradient(180deg,#f1f1f1,#e6e6e6)"></div><h4>Product Name 2</h4><div class="price">$ 61.19</div><a class="add">Add to Cart</a></div>

<div class="promo"><h3>COMPUTER<br>ACCESSORIES</h3><div class="device" role="img" aria-label="Desktop, tablet and laptop devices"></div><a class="shop">SHOP NOW</a></div>

<div class="section-head" style="top:1551px"><h2>TOP SELLING PRODUCTS</h2><div class="rule" style="width:231px"></div></div>
<div class="pager" style="top:1569px"><span><svg width="8" height="12"><path d="M7 1L2 6l5 5" fill="none" stroke="#333" stroke-width="1.5"/></svg></span><span><svg width="8" height="12"><path d="M1 1l5 5-5 5" fill="none" stroke="#333" stroke-width="1.5"/></svg></span></div>

<div class="card rated" style="left:159px;top:1633px"><div class="img" role="img" aria-label="Engraved gold and silver bangles" style="background:linear-gradient(180deg,#ece8e2,#f4f2ef)"></div><h4>Gift Ring for Love</h4><div class="price">$ 61.19</div><div class="stars">★★★★☆</div><a class="add">Add to Cart</a></div>
<div class="card rated" style="left:386px;top:1633px"><div class="img" role="img" aria-label="Yellow ruler, pencils and sharpener" style="background:linear-gradient(135deg,#f4f1d8,#f3d54a 60%,#f1efe5)"></div><h4>Stationery Item1</h4><div class="price">$ 61.19</div><div class="stars">★★★★☆</div><a class="add">Add to Cart</a></div>
<div class="card rated" style="left:612px;top:1633px"><div class="img" role="img" aria-label="Colourful colouring gift set" style="background:linear-gradient(135deg,#f48bb1,#e23d7a 50%,#f6c0d4)"></div><h4 style="margin-top:20px;padding-bottom:12px">Coloring gift set</h4><div class="price">$ 61.19</div><div class="stars">★★★★☆</div><a class="add">Add to Cart</a></div>
<div class="card rated" style="left:838px;top:1633px"><div class="img" role="img" aria-label="Books tied with a red ribbon" style="background:linear-gradient(180deg,#ededeb,#d83a3a 45%,#e9dccb)"></div><h4>Text Book Gift</h4><div class="price">$ 61.19</div><div class="stars">★★★★☆</div><a class="add">Add to Cart</a></div>

<div class="divider"></div>

<div class="section-head" style="top:2139px"><h2>LATEST NEWS</h2><div class="rule" style="width:278px"></div></div>

<article class="news" style="left:162px"><div class="img" role="img" aria-label="Stack of novels" style="background:linear-gradient(135deg,#2a3a5c,#a84a5c 50%,#d9cfa8)"><div class="date">02<small>FEB</small></div></div><h5>CURABITUR LIGULASAPIEN</h5><p>Vestibulum sagittis, nisl nec pellentesque suscipit, arcu nisi maximus neque, vitae finibus erat odio eu lacus. Curabitur male-suada erat erosnec.</p></article>
<article class="news" style="left:461px"><div class="img" role="img" aria-label="Pink stationery set" style="background:linear-gradient(135deg,#f1e4e8,#e8559a 50%,#f3b3cc)"><div class="date">02<small>FEB</small></div></div><h5 style="margin-left:8px">CURABITUR LIGULASAPIEN</h5><p style="margin-left:8px">Vestibulum sagittis, nisl nec pellentesque suscipit, arcu nisi maximus neque, vitae finibus erat odio eu lacus. Curabitur male-suada erat erosturpis nec.</p></article>
<article class="news" style="left:760px"><div class="img" role="img" aria-label="Laptop repair on a workbench" style="background:linear-gradient(135deg,#e4e8ee,#9aa4b2 50%,#3a3f48)"><div class="date">02<small>FEB</small></div></div><h5>CURABITUR LIGULASAPIEN</h5><p>Vestibulum sagittis, nisl nec pellentesque suscipit, arcu nisi maximus neque, vitae finibus erat odio eu lacus. Curabitur male-suada erat eros, quisimpen.</p></article>

<footer class="site-footer">
  <div class="foot-brand">Unicampus<br>Store<small>EST. 1968</small></div>
  <p class="foot-about">Vestibulum sagittis, nisl nec pellen-tesque suscipit, arcu nisi maximus neque, vitae finibus erat odio eu lacus. Curabitur malesuada erat eros, quis dignissim dui accumsan id. Cras non imperdiet metus. Sed nec turpis nec.</p>
  <div class="newsletter"><h6>SIGN UP FOR OUR NEWSLETTER !</h6><div class="email">Email Address</div><div class="submit">SUBMIT</div></div>
  <div class="foot-rule"></div>
  <div class="foot-col" style="left:418px"><h6>INFORMATION</h6><ul><li>About Us</li><li>FAQ</li><li>Products</li><li>Latest News</li></ul></div>
  <div class="foot-col" style="left:606px"><h6>CUSTOMER CARE</h6><ul><li>Returns</li><li>Shipping Info</li><li>Terms and Conditions</li><li>Policies</li></ul></div>
  <div class="foot-col" style="left:794px"><h6>CONTACT US</h6>
    <div class="contact-row"><svg viewBox="0 0 12 14"><path d="M6 0a5 5 0 0 1 5 5c0 4-5 9-5 9S1 9 1 5a5 5 0 0 1 5-5z" fill="#f0b90b"/><circle cx="6" cy="5" r="2" fill="#1f2a63"/></svg><span>Lorem ipsum dolor sit amet,<br>Onsectetuer adipiscing elit.</span></div>
    <div class="contact-row"><svg viewBox="0 0 12 14"><rect x="0" y="3" width="12" height="8" fill="#f0b90b"/><path d="M0 3l6 5 6-5" fill="none" stroke="#1f2a63" stroke-width="1.2"/></svg><span>hello@unicampusstore.edu</span></div>
    <div class="contact-row"><svg viewBox="0 0 12 14"><path d="M2 1l3 3-1.5 2a8 8 0 0 0 4 4L9 8.5l3 3-2 2C5 13 0 8 0 3z" fill="#f0b90b"/></svg><span>0123.456.789</span></div>
  </div>
  <div class="foot-bottom"></div>
  <div class="copyright">Unicampus Store © 2020. All Rights Reserved</div>
  <div class="foot-social" aria-label="Social media links"><span></span><span></span><span></span><span></span></div>
</footer>

</body>
</html>
```